Autobody repair paint repairs spray painting bodywork crash repairs

Details for my new Facebook Design Project will be added sooAUTOMOTIVE REPAIR. CAR / MOTORCYCLES GOT LOGO DESIGN / DID THINK ABOUT FACEBOOK DONT NOALREADY HAVE WEB ADRESS www.brightpanel.co.uk and mail sales@brightpanel,co.uk NEED SOMETHINK I CAN MANAGE TO UPLOAD PICTURES IN TO A GALLERY OR SOMETHINGLIKE THAT I ALSO SELL CAR AND MOTORCYCLES MAYBE A SELLS PAGE WITH A COINDROP LINKn.
Updates

Target Market(s)

general public and trade

Industry/Entity Type

Auto Repair

Font styles to use
Serif
Sans Serif

Colors

Designer to choose colors to be used in the design.

Requirements
Must have
• copy description from my website
• coindrop link. to my site shop
• plenty of logo within reason
Nice to have
• scolling shop
• easy to manage

```html
<!DOCTYPE html>
<html lang="en">
<head>
<meta charset="UTF-8">
<title>Brightpanel Bodyshop</title>
<link rel="stylesheet" href="https://fonts.googleapis.com/css2?family=Montserrat:wght@300;400;500;600;700&display=swap">
<style>
  :root {
    --navy: #0a1150;
    --black: #000000;
    --silver-light: #d4d4d4;
    --silver-dark: #6a6a6a;
    --red: #fe1414;
    --white: #ffffff;
    --text-soft: #e6e8f2;
  }
  html, body {
    margin: 0;
    padding: 0;
    width: 1200px;
    height: 581px;
    overflow: hidden;
    background: var(--navy);
  }
  .banner {
    position: relative;
    width: 1200px;
    height: 581px;
    background: var(--navy);
    font-family: "Montserrat", sans-serif;
    color: var(--white);
    overflow: hidden;
  }
  .chevron {
    position: absolute;
    inset: 0;
    width: 1200px;
    height: 581px;
  }
  .car-photo {
    position: absolute;
    left: 0;
    top: 140px;
    width: 552px;
    height: 310px;
    background: radial-gradient(ellipse at 55% 50%, #3a3a3a 0%, #1c1c1c 45%, #050505 80%);
    border-radius: 40px 120px 30px 10px;
  }
  .brand {
    position: absolute;
    right: 82px;
    top: 98px;
    width: 420px;
    text-align: center;
  }
  .brand-name {
    display: block;
    font-size: 42px;
    font-weight: 600;
    letter-spacing: 3px;
    color: var(--silver-light);
    line-height: 1;
  }
  .brand-sub {
    display: block;
    margin-top: 20px;
    font-size: 18px;
    font-weight: 500;
    letter-spacing: 11.5px;
    color: var(--white);
    padding-left: 12px;
  }
  .headline {
    position: absolute;
    right: 82px;
    top: 210px;
    margin: 0;
    text-align: right;
    font-weight: 400;
  }
  .headline-top {
    display: block;
    font-size: 32px;
    letter-spacing: 2.5px;
    line-height: 44px;
  }
  .headline-accent {
    display: block;
    font-size: 35px;
    font-weight: 700;
    color: var(--red);
    letter-spacing: 0.5px;
    line-height: 44px;
  }
  .intro {
    position: absolute;
    right: 90px;
    top: 314px;
    width: 340px;
    margin: 0;
    text-align: right;
    font-size: 12.8px;
    font-weight: 300;
    letter-spacing: 0.5px;
    line-height: 23px;
    color: var(--text-soft);
  }
  .cta {
    position: absolute;
    left: 837px;
    top: 418px;
    width: 281px;
    height: 51px;
    background: var(--red);
    color: var(--white);
    font-size: 17.5px;
    font-weight: 600;
    letter-spacing: 0.5px;
    display: flex;
    align-items: center;
    justify-content: center;
    text-decoration: none;
  }
  .contact {
    position: absolute;
    top: 526px;
    display: flex;
    align-items: center;
    gap: 9px;
    font-size: 15px;
    font-weight: 400;
    letter-spacing: 0.3px;
    color: var(--white);
  }
  .contact-web { left: 226px; }
  .contact-mail { left: 606px; }
  .contact-icon { width: 17px; height: 17px; }
</style>
</head>
<body>
  <main class="banner">
    <svg class="chevron" viewBox="0 0 1200 581" aria-hidden="true">
      <defs>
        <linearGradient id="silverBand" x1="0" y1="0" x2="0" y2="1">
          <stop offset="0" stop-color="#8a8a8a"/>
          <stop offset="0.5" stop-color="#d8d8d8"/>
          <stop offset="1" stop-color="#555555"/>
        </linearGradient>
      </defs>
      <polygon points="0,0 520,0 684,290.5 520,581 0,581" fill="url(#silverBand)"/>
      <polygon points="0,0 478,0 648,290.5 478,581 0,581" fill="var(--black)"/>
    </svg>

    <div class="car-photo" role="img" aria-label="Photo of a black luxury saloon car, front three-quarter view, lit against a dark background"></div>

    <div class="brand">
      <span class="brand-name">BRIGHTPANEL</span>
      <span class="brand-sub">BODYSHOP</span>
    </div>

    <h1 class="headline">
      <span class="headline-top">YOUR ONE STOP</span>
      <span class="headline-accent">BODYSHOP</span>
    </h1>

    <p class="intro">From the repair of the smallest dents and scratches to major auto repair work, Brightpanel is set up to meet your needs</p>

    <a class="cta" href="#">GET STARTED</a>

    <div class="contact contact-web">
      <svg class="contact-icon" viewBox="0 0 20 20" aria-hidden="true">
        <g fill="none" stroke="var(--red)" stroke-width="1.6">
          <circle cx="10" cy="10" r="8.5"/>
          <ellipse cx="10" cy="10" rx="3.8" ry="8.5"/>
          <line x1="1.5" y1="10" x2="18.5" y2="10"/>
          <line x1="3" y1="5.5" x2="17" y2="5.5"/>
          <line x1="3" y1="14.5" x2="17" y2="14.5"/>
        </g>
      </svg>
      <span>www.brightpanel.co.uk</span>
    </div>

    <div class="contact contact-mail">
      <svg class="contact-icon" viewBox="0 0 20 20" aria-hidden="true">
        <rect x="1" y="4" width="18" height="12" fill="var(--red)"/>
        <polyline points="1,4 10,11 19,4" fill="none" stroke="var(--navy)" stroke-width="1.4"/>
      </svg>
      <span>sales@brightpanel.co.uk</span>
    </div>
  </main>
</body>
</html>
```